Waschkarten-Design für Tankstelle gesucht
Zielgruppe
Unsere Tankstelle hat in eine neue Waschanlage investiert. Die Alten Waschkarten gefallen nicht mehr, und sind auch mit der Programmstruktur nicht mehr kompatibel. Siehe Anhang.
Waschkunden in der Portalwaschanlage jeglichen Alters und Geschlechts.
Aufgabenstellung
Wertigkeit der einzelnen Waschprogramme muss erkennbar sein. Beschriftung z. B. Mehrfachwäschen 3er 5er 10er bzw. Wertkarten der Preis soll veränderbar sein, so das die Karten jederzeit angepasst werden können. Auch sollte der Programm-Name von uns selbst geändert werden können. Die Einschiebe Richtung muss klar erkennbar sein.
Das Design muss im Check-Kartenformat sein. Achtung abgerundete Ecken mit ca. r=2 mm
Anbei ein Bild von unserer Neuen Waschanlage

```html
<!DOCTYPE html>
<html lang="de">
<head>
<meta charset="utf-8">
<title>Waschkarten – Express, Top, Premium</title>
<link rel="stylesheet" href="https://fonts.googleapis.com/css2?family=Anton&family=Ubuntu:wght@300;500&display=swap">
<style>
  :root {
    --frame: #0d4a5c;
    --paper: #ffffff;
    --ink-light: #fdf9f0;
    --ink-dark: #1a1410;
    --teal: #6f9c98;
    --slate: #5f8296;
    --amber: #c98a4a;
    --rust: #a4583a;
    --olive: #b89a3c;
  }
  * { margin: 0; padding: 0; box-sizing: border-box; }
  html, body { width: 1200px; height: 1200px; overflow: hidden; background: var(--paper); }
  .canvas {
    position: relative;
    width: 1200px; height: 1200px;
    border: 6px solid var(--frame);
    background: var(--paper);
  }
  .wash-card {
    position: absolute;
    left: 353px;
    width: 481px; height: 304px;
    overflow: hidden;
    border-radius: 2px;
  }
  .wash-card--express { top: 126px; }
  .wash-card--top { top: 442px; }
  .wash-card--premium { top: 758px; }

  .scene-fill { position: absolute; inset: 0; }
  .wash-card--express .scene-fill {
    background:
      radial-gradient(ellipse at 70% 45%, rgba(232,180,120,.55), transparent 60%),
      linear-gradient(120deg, var(--teal) 0%, var(--amber) 45%, var(--rust) 60%, var(--amber) 80%, var(--teal) 100%);
  }
  .wash-card--top .scene-fill {
    background:
      radial-gradient(ellipse at 65% 40%, rgba(120,170,150,.6), transparent 60%),
      linear-gradient(120deg, var(--teal) 0%, var(--olive) 45%, var(--rust) 60%, var(--olive) 85%, var(--teal) 100%);
  }
  .wash-card--premium .scene-fill {
    background:
      radial-gradient(ellipse at 70% 45%, rgba(200,150,110,.5), transparent 60%),
      linear-gradient(120deg, var(--slate) 0%, var(--amber) 45%, var(--rust) 60%, var(--slate) 85%, var(--amber) 100%);
  }

  .insert-arrow { position: absolute; left: 0; top: 0; width: 481px; height: 304px; }

  .program-name {
    position: absolute;
    left: 20px; top: 4px;
    font-family: "Anton", sans-serif;
    font-weight: 400;
    line-height: 1;
    color: var(--ink-light);
    transform-origin: top left;
    letter-spacing: -1px;
    white-space: nowrap;
  }
  .wash-card--express .program-name { font-size: 98px; transform: scaleY(1.6); }
  .wash-card--top .program-name { left: 18px; top: 7px; font-size: 90px; transform: scaleY(1.75); }
  .wash-card--premium .program-name { left: 20px; top: 4px; font-size: 91px; transform: scaleY(1.73); }

  .program-detail {
    position: absolute;
    right: 30px; top: 153px;
    font-family: "Ubuntu", sans-serif;
    font-weight: 300;
    font-size: 32px;
    line-height: 1.12;
    color: var(--ink-light);
    text-align: right;
    white-space: nowrap;
  }
  .wash-card--express .program-detail { right: 34px; }

  .program-price {
    position: absolute;
    right: 30px; top: 218px;
    font-family: "Ubuntu", sans-serif;
    font-weight: 300;
    font-size: 64px;
    line-height: 1;
    color: var(--ink-light);
    white-space: nowrap;
  }
  .wash-card--express .program-price { right: 32px; }
  .wash-card--top .program-price,
  .wash-card--premium .program-price { right: 26px; }

  .brand-disc {
    position: absolute;
    left: -42px; top: 184px;
    width: 236px; height: 236px;
    border-radius: 50%;
    background: rgba(255,255,255,.62);
  }
  .brand-name {
    position: absolute;
    left: 22px; top: 222px;
    font-family: "Ubuntu", sans-serif;
    font-weight: 500;
    font-size: 24px;
    line-height: 1.1;
    color: var(--ink-dark);
  }
</style>
</head>
<body>
<main class="canvas">

  <section class="wash-card wash-card--express">
    <div class="scene-fill" role="img" aria-label="Pop-Art-Illustration: Frau poliert ein Auto vor einem Strahlenmuster in Orange und Petrol"></div>
    <svg class="insert-arrow" viewBox="0 0 481 304" aria-hidden="true">
      <path d="M220 48 H341 V28 L447 89 L341 150 V120 H220 Z" fill="#ffffff" fill-opacity=".5"/>
    </svg>
    <h2 class="program-name">EXPRESS</h2>
    <p class="program-detail">Waschen und Trocknen</p>
    <p class="program-price">€ 5,95</p>
    <div class="brand-disc"></div>
    <p class="brand-name">Tankstelle<br>Lindner</p>
  </section>

  <section class="wash-card wash-card--top">
    <div class="scene-fill" role="img" aria-label="Pop-Art-Illustration: Frau poliert ein Auto vor einem Strahlenmuster in Ocker und Petrol"></div>
    <svg class="insert-arrow" viewBox="0 0 481 304" aria-hidden="true">
      <path d="M233 57 H352 V27 L458 89 L352 151 V119 H233 Z" fill="#ffffff" fill-opacity=".5"/>
    </svg>
    <h2 class="program-name">TOP</h2>
    <p class="program-detail">Wachs und Unterboden</p>
    <p class="program-price">€ 12,95</p>
    <div class="brand-disc"></div>
    <p class="brand-name">Tankstelle<br>Lindner</p>
  </section>

  <section class="wash-card wash-card--premium">
    <div class="scene-fill" role="img" aria-label="Pop-Art-Illustration: Frau poliert ein Auto vor einem Strahlenmuster in Blaugrau und Orange"></div>
    <svg class="insert-arrow" viewBox="0 0 481 304" aria-hidden="true">
      <path d="M233 58 H352 V27 L458 89 L352 151 V120 H233 Z" fill="#ffffff" fill-opacity=".5"/>
    </svg>
    <h2 class="program-name">PREMIUM</h2>
    <p class="program-detail">Politurprogramm mit<br>Unterbodenwäsche</p>
    <p class="program-price">€ 16,95</p>
    <div class="brand-disc"></div>
    <p class="brand-name">Tankstelle<br>Lindner</p>
  </section>

</main>
</body>
</html>
```